Belford & Company

We are a boutique commercial real estate firm. For our Business card design - sleek, modern, yet high-end/classy. Please see our website: belfordandcompany.example for details.

We currently need 2 business card names and the ability to add/change the business card information -
Name, Title, Address, Office #, Mobile #, Fax, Email and company website.

Industry/Entity Type

Real Estate

Contact Information for Business Card

Business card design - sleek, modern, yet high-end/classy. Please see our website: belfordandcompany.example for details.

Also, we'd like to have our slogan "Precision Shapes Every Outcome." somewhere in there. We'd like to make some part of it raised or a different texture if possible.
Color #'s:
blue 19 36 128
light gray 222 222 221
dark gray 107 120 128

Also, we'd like to have our slogan "Precision Shapes Every Outcome." somewhere in there. We'd like to make some part of it raised or a different texture if possible - grey on one side and blue on the other - rounded edges preferred. Maybe either metal/silver/grey raised logo on the back. Thank you!!

Requirements
Must have
• Sleek, modern, clean and classy design

```html
<!DOCTYPE html>
<html lang="en">
<head>
<meta charset="utf-8">
<title>Belford &amp; Company – Business Card</title>
<link rel="stylesheet" href="https://fonts.googleapis.com/css2?family=Kanit:wght@400;500;600&display=swap">
<style>
  :root {
    --brand-blue: #13247f;
    --bright-blue: #1b6bc4;
    --mid-blue: #1a3f9e;
    --light-gray: #dededd;
    --dark-gray: #6b7880;
    --frame-gray: #8793a0;
    --page-bg: #f2f2f2;
    --white: #ffffff;
  }
  * { box-sizing: border-box; margin: 0; padding: 0; }
  html, body {
    width: 1200px; height: 1200px; overflow: hidden;
    background: var(--page-bg);
    font-family: "Kanit", sans-serif;
  }
  .canvas { position: relative; width: 1200px; height: 1200px; }

  .card { position: absolute; overflow: hidden; border-radius: 44px; }

  /* Front */
  .card-front {
    left: 150px; top: 42px; width: 900px; height: 540px;
    background: var(--brand-blue);
  }
  .front-name {
    position: absolute; left: 0; right: 0; top: 246px;
    text-align: center; color: var(--white);
    font-weight: 600; font-size: 46px; letter-spacing: 1px;
  }
  .front-name .mark-square {
    display: inline-block; width: 26px; height: 26px;
    background: var(--white); margin-right: 16px; vertical-align: 2px;
  }
  .slogan {
    position: absolute; left: 0; right: 0; top: 456px;
    text-align: center; color: var(--white);
    font-weight: 500; font-size: 18px; letter-spacing: .3px;
  }

  /* Back */
  .card-back {
    left: 156px; top: 618px; width: 888px; height: 540px;
    background: var(--dark-gray);
  }
  .decor-band {
    position: absolute; left: 0; right: 0; bottom: 0; height: 130px;
    background: linear-gradient(100deg, var(--brand-blue), var(--mid-blue) 50%, var(--bright-blue));
  }
  .logo-frame {
    position: absolute; left: 74px; top: 101px; width: 329px; height: 183px;
    border: 2px solid var(--frame-gray);
    display: flex; align-items: center; justify-content: center;
  }
  .logo-name {
    color: var(--white); font-weight: 600; font-size: 30px; letter-spacing: .5px;
  }
  .divider {
    position: absolute; left: 455px; top: 72px; width: 3px; height: 316px;
    background: linear-gradient(to bottom, rgba(222,222,221,0), var(--light-gray) 20%, var(--light-gray) 80%, rgba(222,222,221,0));
  }
  .contact { position: absolute; left: 494px; top: 90px; color: var(--light-gray); }
  .person-name {
    color: var(--brand-blue); font-weight: 600; font-size: 34px; line-height: 38px;
  }
  .person-title { font-size: 16px; font-weight: 500; line-height: 18px; }
  .address { margin-top: 22px; font-size: 19px; font-weight: 500; line-height: 31px; }
  .contact-list { list-style: none; margin-top: 10px; }
  .contact-list li {
    display: flex; align-items: center; height: 30px;
    font-size: 19px; font-weight: 500;
  }
  .contact-list svg { width: 22px; height: 22px; margin-right: 24px; fill: none; stroke: var(--light-gray); stroke-width: 1.6; }
</style>
</head>
<body>
<div class="canvas">

  <section class="card card-front">
    <div class="front-name"><span class="mark-square"></span>Belford &amp; Company</div>
    <p class="slogan">Precision Shapes Every Outcome</p>
  </section>

  <section class="card card-back">
    <div class="decor-band" role="img" aria-label="Decorative blue band along the bottom edge"></div>

    <div class="logo-frame">
      <span class="logo-name">Belford &amp; Company</span>
    </div>

    <div class="divider"></div>

    <div class="contact">
      <h1 class="person-name">MARCUS ELLERY</h1>
      <p class="person-title">Managing Director</p>
      <p class="address">2480 Harbor Ridge Blvd., Suite #310<br>Riverton, FL 32100</p>
      <ul class="contact-list">
        <li><svg viewBox="0 0 24 24"><rect x="7" y="2" width="10" height="20" rx="1.5"/><line x1="11" y1="19" x2="13" y2="19"/></svg>(555) 014-2287</li>
        <li><svg viewBox="0 0 24 24"><path d="M3 9c0-3 18-3 18 0v2h-5V9H8v2H3z"/><rect x="5" y="13" width="14" height="8" rx="1"/><circle cx="12" cy="16" r="1.6"/></svg>(555) 018-3391</li>
        <li><svg viewBox="0 0 24 24"><rect x="2" y="5" width="20" height="14" fill="#dededd"/><path d="M2 5l10 8 10-8" stroke="#6b7880"/></svg>info@belfordandcompany.example</li>
        <li><svg viewBox="0 0 24 24"><circle cx="12" cy="12" r="9.5"/><ellipse cx="12" cy="12" rx="4" ry="9.5"/><line x1="2.5" y1="12" x2="21.5" y2="12"/></svg>www.belfordandcompany.example</li>
      </ul>
    </div>
  </section>

</div>
</body>
</html>
```